I'm a magician . hypnotist also a good barber. I need this all to be shown in good detail on the cards.

Industry/Entity Type

Magician

Contact Information for Business Card

Magician/ hypnotist/barber Rowan Pitt. One of the best. Tel 07421 736204
Email.Trickshears48@fernmail.example
Title of card spell chap.

```html
<!DOCTYPE html>
<html lang="en">
<head>
<meta charset="utf-8">
<title>Spell Chap – Rowan Pitt</title>
<link rel="stylesheet" href="https://fonts.googleapis.com/css2?family=Libre+Baskerville:wght@700&family=Marcellus&family=Noto+Sans:wght@400&display=swap">
<style>
  :root {
    --brand-blue: #0080ff;
    --emblem-blue: #1a82ff;
    --ink: #000000;
    --paper-light: #ffffff;
    --paper-mid: #dcdcdc;
    --paper-dark: #bababa;
    --band-text: #ffffff;
  }
  html, body {
    margin: 0;
    padding: 0;
    width: 1200px;
    height: 791px;
    overflow: hidden;
  }
  .business-card {
    position: relative;
    width: 1200px;
    height: 791px;
    overflow: hidden;
    background: radial-gradient(ellipse 1100px 900px at 0px 380px, var(--paper-light) 0%, var(--paper-mid) 45%, var(--paper-dark) 100%);
  }
  .contact-row {
    position: absolute;
    top: 64px;
    left: 42px;
    right: 45px;
    display: flex;
    justify-content: space-between;
    font-family: "Libre Baskerville", serif;
    font-weight: 700;
    font-size: 30px;
    color: var(--ink);
    text-transform: uppercase;
    letter-spacing: 0.5px;
  }
  .emblem {
    position: absolute;
    left: 398px;
    top: 95px;
    width: 405px;
    height: 407px;
  }
  .email {
    position: absolute;
    top: 540px;
    left: 0;
    width: 1200px;
    text-align: center;
    font-family: "Noto Sans", sans-serif;
    font-size: 31px;
    color: var(--emblem-blue);
  }
  .title-band {
    position: absolute;
    left: 0;
    top: 614px;
    width: 1200px;
    height: 177px;
    background: var(--brand-blue);
    display: flex;
    align-items: baseline;
    gap: 8px;
    padding: 0 0 0 42px;
    box-sizing: border-box;
    color: var(--band-text);
  }
  .card-title {
    font-family: "Marcellus", serif;
    font-size: 92px;
    line-height: 1;
    margin: 0;
    font-weight: 400;
    padding-top: 32px;
    text-transform: uppercase;
    white-space: nowrap;
  }
  .services {
    font-family: "Noto Sans", sans-serif;
    font-size: 21px;
    text-transform: uppercase;
    white-space: nowrap;
    position: relative;
    top: -22px;
  }
</style>
</head>
<body>
  <div class="business-card">
    <div class="contact-row">
      <span class="owner-name">Rowan Pitt</span>
      <span class="phone">Tel: 07421 736204</span>
    </div>

    <svg class="emblem" viewBox="0 0 405 407" role="img" aria-label="Emblem illustration: a top hat above barber scissors standing in rippling rings">
      <defs>
        <radialGradient id="emblemTone" cx="50%" cy="50%" r="60%">
          <stop offset="0%" stop-color="#1a82ff" stop-opacity="0.55"/>
          <stop offset="100%" stop-color="#1a82ff" stop-opacity="0.15"/>
        </radialGradient>
      </defs>
      <rect x="0" y="0" width="405" height="407" rx="24" fill="url(#emblemTone)"/>
    </svg>

    <p class="email" style="margin:0">Email: Trickshears48@fernmail.example</p>

    <div class="title-band">
      <h1 class="card-title">Spell Chap</h1>
      <span class="services">Magician/ Hypnotist/Barber</span>
    </div>
  </div>
</body>
</html>
```